Pelbrook Business Cards

Create new business cards with the details below.

Aaron Velst
Director

MB: +61 412 563 904
PH: 1300 417 639
Email: aaron.velst@pelbrook.com.au
Address: 27C Marlow Parade, Brennwick SA 5112 Australia
Website: www.pelbrook.com.au

Target Market(s)

Other business

Industry/Entity Type

Business

Requirements
Must have
• must be clean looking

```html
<!DOCTYPE html>
<html lang="en">
<head>
<meta charset="utf-8">
<title>Pelbrook Business Cards</title>
<link rel="stylesheet" href="https://fonts.googleapis.com/css2?family=Roboto:wght@400;700;900&display=swap">
<style>
  :root {
    --lime: #a6cc3a;
    --lime-light: #c3dd66;
    --lime-dark: #8fb82c;
    --charcoal: #333537;
    --ink: #3b3d40;
    --white: #ffffff;
    --page: #e9e9e6;
  }
  * { box-sizing: border-box; margin: 0; padding: 0; }
  html, body { width: 1200px; height: 1000px; overflow: hidden; }
  body {
    background: var(--page);
    font-family: "Roboto", Arial, sans-serif;
    position: relative;
  }
  .card {
    position: absolute;
    left: 250px;
    width: 700px;
    height: 428px;
    border-radius: 56px 0 0 0;
    overflow: hidden;
    box-shadow: 0 10px 28px rgba(0,0,0,.18);
  }

  /* Front */
  .card-front {
    top: 48px;
    background: linear-gradient(160deg, var(--lime-light) 0%, var(--lime) 70%, var(--lime-dark) 100%);
  }
  .front-brand {
    position: absolute;
    left: 46px;
    bottom: 40px;
    color: var(--ink);
  }
  .brand-name {
    font-weight: 900;
    font-size: 40px;
    letter-spacing: 0.5px;
    line-height: 1;
    text-transform: uppercase;
  }
  .brand-tagline {
    font-weight: 700;
    font-size: 15.5px;
    letter-spacing: 1px;
    margin-top: 4px;
    text-transform: uppercase;
  }

  /* Back */
  .card-back {
    top: 524px;
    background: var(--white);
  }
  .back-header {
    height: 128px;
    position: relative;
    padding: 40px 44px 0 40px;
    display: flex;
    justify-content: space-between;
  }
  .logo-lockup { display: flex; align-items: center; gap: 12px; }
  .logo-square { width: 38px; height: 38px; background: var(--lime); }
  .logo-text .brand-name { font-size: 32px; color: var(--ink); }
  .logo-text .brand-tagline { font-size: 12.5px; color: var(--ink); margin-top: 2px; }
  .person { text-align: right; color: var(--ink); }
  .person-name { font-size: 16px; font-weight: 400; }
  .person-title { font-size: 16px; font-weight: 700; letter-spacing: .5px; }

  .contact-band {
    height: 206px;
    background: var(--lime);
    display: flex;
    padding: 54px 44px 0 44px;
    gap: 60px;
    color: var(--white);
    font-size: 15px;
  }
  .contact-col { list-style: none; }
  .contact-col li { display: flex; align-items: flex-start; gap: 12px; margin-bottom: 12px; line-height: 1.45; }
  .contact-col svg { width: 15px; height: 15px; flex: none; margin-top: 3px; fill: var(--charcoal); }
  .contact-col.right { margin-left: auto; }

  .web-band {
    height: 94px;
    background: var(--charcoal);
    display: flex;
    align-items: center;
    padding-left: 300px;
    color: var(--white);
    font-weight: 700;
    font-size: 20px;
    letter-spacing: .3px;
  }
</style>
</head>
<body>

  <section class="card card-front" aria-label="Business card front">
    <div class="front-brand">
      <div class="brand-name">Pelbrook</div>
      <div class="brand-tagline">Plantation Shutters</div>
    </div>
  </section>

  <section class="card card-back" aria-label="Business card back">
    <header class="back-header">
      <div class="logo-lockup">
        <div class="logo-square"></div>
        <div class="logo-text">
          <div class="brand-name">Pelbrook</div>
          <div class="brand-tagline">Plantation Shutters</div>
        </div>
      </div>
      <div class="person">
        <div class="person-name">Aaron Velst</div>
        <div class="person-title">DIRECTOR</div>
      </div>
    </header>

    <div class="contact-band">
      <ul class="contact-col">
        <li>
          <svg viewBox="0 0 24 24" aria-hidden="true"><path d="M6.6 10.8a15 15 0 0 0 6.6 6.6l2.2-2.2a1 1 0 0 1 1-.25 11.4 11.4 0 0 0 3.6.57 1 1 0 0 1 1 1V20a1 1 0 0 1-1 1A17 17 0 0 1 3 4a1 1 0 0 1 1-1h3.5a1 1 0 0 1 1 1c0 1.25.2 2.45.57 3.57a1 1 0 0 1-.25 1z"/></svg>
          <span>1300 417 639</span>
        </li>
        <li>
          <svg viewBox="0 0 24 24" aria-hidden="true"><path d="M7 1h10a2 2 0 0 1 2 2v18a2 2 0 0 1-2 2H7a2 2 0 0 1-2-2V3a2 2 0 0 1 2-2zm0 3v14h10V4zm5 15.2a1 1 0 1 0 0 2 1 1 0 0 0 0-2z"/></svg>
          <span>+61 412 563 904</span>
        </li>
        <li>
          <svg viewBox="0 0 24 24" aria-hidden="true"><path d="M2 5h20v14H2zm2 2v.5l8 5 8-5V7zm0 2.8V17h16V9.8l-8 5z"/></svg>
          <span>aaron.velst@pelbrook.com.au</span>
        </li>
      </ul>
      <ul class="contact-col right">
        <li>
          <svg viewBox="0 0 24 24" aria-hidden="true"><path d="M12 2a7 7 0 0 0-7 7c0 5.2 7 13 7 13s7-7.8 7-13a7 7 0 0 0-7-7zm0 9.5A2.5 2.5 0 1 1 12 6.5a2.5 2.5 0 0 1 0 5z"/></svg>
          <span>27C Marlow Parade, Brennwick<br>SA 5112 Australia</span>
        </li>
        <li>
          <svg viewBox="0 0 24 24" aria-hidden="true"><path d="M12 2a10 10 0 1 0 0 20 10 10 0 0 0 0-20zm6.9 9h-3a15 15 0 0 0-1.3-5.4A8 8 0 0 1 18.9 11zM12 4.1c.9 1.3 1.7 3.6 1.9 6.9h-3.8c.2-3.3 1-5.6 1.9-6.9zM9.4 5.6A15 15 0 0 0 8.1 11h-3a8 8 0 0 1 4.3-5.4zM5.1 13h3a15 15 0 0 0 1.3 5.4A8 8 0 0 1 5.1 13zm6.9 6.9c-.9-1.3-1.7-3.6-1.9-6.9h3.8c-.2 3.3-1 5.6-1.9 6.9zm2.6-1.5a15 15 0 0 0 1.3-5.4h3a8 8 0 0 1-4.3 5.4z"/></svg>
          <span>www.pelbrook.com.au</span>
        </li>
      </ul>
    </div>

    <footer class="web-band">www.pelbrook.com.au</footer>
  </section>

</body>
</html>
```